Selbsthilfegruppe für organtransplantierte Personen sucht Flyer-Design
Sehr schnelle Reaktion auf Änderungswünsche und top Support bis zum Druck :) Gerne wieder!
Zielgruppe
Wir sind eine Selbsthilfegruppe für organtransplantierte Personen, Zielgruppe sind Personen aus der Region die auch ein Spenderorgan empfangen haben und deren Angehörige, die Beistand und Information suchen sowie gemeinsame Aktivitäten wahrnehmen möchten.
Aufgabenstellung
Es gibt bereits einen Flyer der jedoch überarbeitet und etwas schöner und moderner gestaltet werden soll. Der Text kann bestehen bleiben und die Aufteilung muss nicht zwingend geändert werden, anstelle der aktuellen Fotos sollen dann andere eingefügt werden, die übergeben werden, sobald das Design akzeptiert wurde. Es geht hauptsächlich um das Design selbst, es soll ansprechen, freundlich, modern und hoffnungsvoll sein, die Grundfarbe sollte grün sein. Das Logo kann beibehalten aber farblich auch gerne angepasst werden. Es soll ein normaler Faltflyer sein, 2 Faltungen und damit vorn und hinten je 3 einzelne Bereiche wie aktuell, Gesamtmaß A4. Bei Rückfragen gerne melden!

```html
<!DOCTYPE html>
<html lang="de">
<head>
<meta charset="utf-8">
<title>Gemeinsam stark – Selbsthilfegruppe Flyer</title>
<link href="https://fonts.googleapis.com/css2?family=Quicksand:wght@500;700&family=Great+Vibes&display=swap" rel="stylesheet">
<style>
  :root{
    --green:#00953a;
    --orange:#ec8a0c;
    --white:#ffffff;
    --stage:#d9d9d9;
    --photo-a:#c9b79a;
    --photo-b:#5f7f5a;
  }
  *{margin:0;padding:0;box-sizing:border-box}
  html,body{width:1200px;height:675px;overflow:hidden;background:var(--stage)}
  .flyer{
    position:absolute;left:157px;top:14px;width:886px;height:626px;
    background:var(--white);overflow:hidden;
    font-family:"Quicksand",sans-serif;color:var(--orange);font-weight:500;
  }
  .flyer__shapes{position:absolute;left:0;top:0}
  .benefits{position:absolute;left:0;top:0;list-style:none}
  .benefits li{
    position:absolute;left:37px;width:260px;font-size:14px;line-height:17.5px;
    transform:translateY(-50%);white-space:nowrap;
  }
  .benefits li::before,.supporters li::before{
    content:"";position:absolute;left:-13px;top:50%;width:9px;height:9px;
    margin-top:-4.5px;border-radius:50%;background:var(--green);
  }
  .contact-title{
    position:absolute;left:388px;top:55px;transform:translate(-50%,-50%);
    font-family:"Great Vibes",cursive;font-size:38px;font-weight:400;
    border-bottom:1px solid var(--orange);line-height:38px;padding:0 2px;
  }
  .photo{position:absolute;border-radius:50%;border:2px solid var(--green)}
  .photo--contact{
    left:321px;top:79px;width:158px;height:158px;
    background:radial-gradient(circle at 55% 45%,#3fae5c,#2f8b45 55%,#c9b360);
  }
  .contact-info{
    position:absolute;left:304px;top:254px;transform:translateY(-50%);
    font-size:15px;font-weight:700;border-bottom:1px solid var(--orange);padding-bottom:2px;
  }
  .support-intro{position:absolute;left:316px;top:291px;transform:translateY(-50%);font-size:14.5px}
  .supporters{position:absolute;left:0;top:0;list-style:none}
  .supporters li{
    position:absolute;left:316px;font-size:14.5px;line-height:19px;
    transform:translateY(-50%);white-space:nowrap;
  }
  .brand{
    position:absolute;left:739px;top:117px;transform:translate(-50%,-50%);
    font-family:"Great Vibes",cursive;font-size:40px;font-weight:400;white-space:nowrap;
    border-bottom:1px solid var(--orange);line-height:38px;padding:0 4px;
  }
  .brand-sub{
    position:absolute;left:739px;top:136px;transform:translateX(-50%);
    text-align:center;font-size:15.5px;line-height:19px;white-space:nowrap;
  }
  .photo--group{
    left:591px;top:178px;width:306px;height:306px;
    background:linear-gradient(160deg,var(--photo-a),#e8d9b8 35%,var(--photo-b) 75%,#3b3f55);
  }
  .offer{
    position:absolute;left:739px;top:558px;transform:translate(-50%,-50%);
    text-align:center;color:var(--white);font-size:17.5px;line-height:23px;white-space:nowrap;
  }
</style>
</head>
<body>
<main class="flyer">
  <svg class="flyer__shapes" width="886" height="626" viewBox="0 0 886 626" aria-hidden="true">
    <path d="M0 0 H411 C260 28 110 62 0 114 Z" fill="var(--green)"/>
    <rect x="591" y="331" width="295" height="295" fill="var(--green)"/>
  </svg>

  <div class="photo photo--group" role="img" aria-label="Gruppenfoto der Mitglieder der Selbsthilfegruppe"></div>

  <svg class="flyer__shapes" width="886" height="626" viewBox="0 0 886 626" aria-hidden="true">
    <path d="M0 571 C300 535 600 478 886 400 V626 H0 Z" fill="var(--green)"/>
  </svg>

  <ul class="benefits">
    <li style="top:131px">Suchen und Finden von<br>Gleichgesinnten</li>
    <li style="top:184px">Einsamkeit durch Gemeinsamkeit<br>überwinden</li>
    <li style="top:229px">Lebenssituation verbessern</li>
    <li style="top:273px">Beziehungen aufbauen<br>und verbessern</li>
    <li style="top:326px">Schwierigkeiten zusammen<br>meistern</li>
    <li style="top:370px">Teilnehmen und verstehen</li>
    <li style="top:405px">Handeln in eigener Sache</li>
    <li style="top:441px">Informationen geben</li>
    <li style="top:476px">Lösungen entdecken und entwickeln</li>
    <li style="top:520px">Freude am Leben finden:<br>Jetzt erst recht!</li>
  </ul>

  <h2 class="contact-title">Kontakt:</h2>
  <div class="photo photo--contact" role="img" aria-label="Foto der Ansprechpartnerin im grünen Gruppen-Shirt an einem Infostand"></div>
  <h3 class="contact-info">Info zum Ansprechpartner:</h3>
  <p class="support-intro">Wir werden unterstützt</p>
  <ul class="supporters">
    <li style="top:338px">von der Deutschen Stiftung<br>Lebensgabe (DSL)</li>
    <li style="top:386px">vom Klinikum Talbrunn: GIZ</li>
    <li style="top:433px">von Fachärzten aus dem Bereich<br>Innere Medizin</li>
    <li style="top:489px">vom Frauenzentrum „Marlene“<br>in Talbrunn</li>
  </ul>

  <h1 class="brand">Gemeinsam stark</h1>
  <p class="brand-sub">Selbsthilfegruppe<br>für Organtransplatation</p>
  <p class="offer">Wir bieten Hilfe für Betroffene<br>sowie Angehörige im Raum<br>Talbrunn an.</p>
</main>
</body>
</html>
```